Modern Attractive Letterhead for Veterinary House Call Business.

A letterhead which can be printed on A4, A5 and A6 paper sizes.
To have: ( our files to be uploaded)
1. Logo with Text
2. telephone
3. email
4. website
5. Address

Target Market(s)

60-85year mainly women pet owners. Also market include families, young professionals, busy people who have dogs and cats

Industry/Entity Type

Business

Requirements
Must have
• 1. Logo with Text ( provided)
• 2. telephone
• 3. email
• 4. website
• 5. Address
Nice to have
• Needs to be modern, preferably warm and caring in nature( if possible )
Should not have
• difficulty in printing A5 and A6

```html
<!DOCTYPE html>
<html lang="en">
<head>
<meta charset="utf-8">
<title>Hearthside Pet Care – Letterhead Set</title>
<link rel="stylesheet" href="https://fonts.googleapis.com/css2?family=Cinzel:wght@500&family=Didact+Gothic&display=swap">
<style>
  :root {
    --backdrop: #d6d6d6;
    --paper: #f4f4f4;
    --ink: #3b3b3b;
    --brand-blue: #2a78b4;
    --wave-green: #7dbb35;
    --wave-green-dark: #5a9e2a;
    --wave-blue: #3796d6;
    --mark-faint: #e7e7e7;
    --icon: #4a5a6a;
  }
  * { box-sizing: border-box; margin: 0; padding: 0; }
  html, body { width: 1200px; height: 1000px; overflow: hidden; }
  body { background: var(--backdrop); position: relative; font-family: "Didact Gothic", sans-serif; }

  .letterhead {
    position: absolute;
    width: 508px; height: 718px;
    background: var(--paper);
    overflow: hidden;
    transform-origin: 0 0;
  }
  .letterhead--a4 { left: 122px; top: 52px; }
  .letterhead--a5 { left: 720px; top: 52px; transform: scale(0.705); }
  .letterhead--a6 { left: 772px; top: 597px; transform: scale(0.5); }

  .brand {
    position: absolute; left: 38px; top: 50px;
    display: flex; align-items: center; gap: 8px;
  }
  .brand__dot { width: 14px; height: 14px; border-radius: 50%; background: var(--brand-blue); }
  .brand__name {
    font-family: "Cinzel", serif; font-weight: 500;
    font-size: 21px; color: var(--brand-blue); letter-spacing: 0.5px;
  }

  .contact {
    position: absolute; left: 359px; top: 51px;
    font-size: 7.5px; line-height: 10px; color: var(--ink);
    list-style: none;
  }
  .contact li { display: flex; align-items: center; gap: 4px; }
  .contact__icon { width: 7px; height: 7px; border-radius: 1.5px; background: var(--icon); }
  .contact__address { margin-top: 8px; font-style: normal; }

  .brand-mark-faint {
    position: absolute; left: 150px; top: 400px;
    width: 290px; height: 290px; border-radius: 50%;
    background: var(--mark-faint);
  }

  .wave { position: absolute; left: 0; bottom: 0; width: 508px; height: 40px; display: block; }
</style>
</head>
<body>

<section class="letterhead letterhead--a4" aria-label="A4 letterhead">
  <div class="brand"><span class="brand__dot"></span><span class="brand__name">Hearthside Pet Care</span></div>
  <ul class="contact">
    <li><span class="contact__icon"></span>0491570110</li>
    <li><span class="contact__icon"></span>hello@hearthsidepets.com.au</li>
    <li><span class="contact__icon"></span>www.hearthsidepets.com.au</li>
    <li><address class="contact__address">PO Box 4410<br>Riverbend QLD 4012</address></li>
  </ul>
  <div class="brand-mark-faint" aria-hidden="true"></div>
  <svg class="wave" viewBox="0 0 508 40" preserveAspectRatio="none" aria-hidden="true">
    <path d="M0 22 C120 12 300 -2 508 10 L508 40 L0 40Z" fill="var(--wave-green)"/>
    <path d="M0 34 C150 24 350 8 508 16 L508 40 L0 40Z" fill="var(--paper)"/>
    <path d="M170 40 C300 26 420 18 508 21 L508 40Z" fill="var(--wave-blue)"/>
  </svg>
</section>

<section class="letterhead letterhead--a5" aria-label="A5 letterhead">
  <div class="brand"><span class="brand__dot"></span><span class="brand__name">Hearthside Pet Care</span></div>
  <ul class="contact">
    <li><span class="contact__icon"></span>0491570110</li>
    <li><span class="contact__icon"></span>hello@hearthsidepets.com.au</li>
    <li><span class="contact__icon"></span>www.hearthsidepets.com.au</li>
    <li><address class="contact__address">PO Box 4410<br>Riverbend QLD 4012</address></li>
  </ul>
  <div class="brand-mark-faint" aria-hidden="true"></div>
  <svg class="wave" viewBox="0 0 508 40" preserveAspectRatio="none" aria-hidden="true">
    <path d="M0 22 C120 12 300 -2 508 10 L508 40 L0 40Z" fill="var(--wave-green)"/>
    <path d="M0 34 C150 24 350 8 508 16 L508 40 L0 40Z" fill="var(--paper)"/>
    <path d="M170 40 C300 26 420 18 508 21 L508 40Z" fill="var(--wave-blue)"/>
  </svg>
</section>

<section class="letterhead letterhead--a6" aria-label="A6 letterhead">
  <div class="brand"><span class="brand__dot"></span><span class="brand__name">Hearthside Pet Care</span></div>
  <ul class="contact">
    <li><span class="contact__icon"></span>0491570110</li>
    <li><span class="contact__icon"></span>hello@hearthsidepets.com.au</li>
    <li><span class="contact__icon"></span>www.hearthsidepets.com.au</li>
    <li><address class="contact__address">PO Box 4410<br>Riverbend QLD 4012</address></li>
  </ul>
  <div class="brand-mark-faint" aria-hidden="true"></div>
  <svg class="wave" viewBox="0 0 508 40" preserveAspectRatio="none" aria-hidden="true">
    <path d="M0 22 C120 12 300 -2 508 10 L508 40 L0 40Z" fill="var(--wave-green)"/>
    <path d="M0 34 C150 24 350 8 508 16 L508 40 L0 40Z" fill="var(--paper)"/>
    <path d="M170 40 C300 26 420 18 508 21 L508 40Z" fill="var(--wave-blue)"/>
  </svg>
</section>

</body>
</html>
```